Homepage web design

I need a homepage design that will be easy to build into a default Word Press theme. Basically, header, navigation, body with sidebar, and footer.

This website is for a small commercial real estate firm in the Washington DC, Maryland and Virginia market.

THIS IS NOT A HOUSING/RESIDENTIAL WEBSITE. PLEASE DO NOT ADD ANY PROPERTY SEARCH FUNCTIONALITY.

Target Market(s)

People looking for basic information about the team and services provided.

Industry/Entity Type

Real Estate

Requirements
Must have
• Professional look. Clean design.

```html
<!DOCTYPE html>
<html lang="en">
<head>
<meta charset="utf-8">
<title>CRB – Commercial Real Estate</title>
<link href="https://fonts.googleapis.com/css2?family=Lato:wght@400;700;900&family=Merriweather:wght@400&display=swap" rel="stylesheet">
<style>
:root{
  --green:#00854a;
  --green-dark:#006a3a;
  --green-deep:#004f2b;
  --ink:#333;
  --muted:#555;
  --line:#d6dcd8;
  --white:#fff;
}
*{margin:0;padding:0;box-sizing:border-box}
html,body{width:1200px;height:960px;overflow:hidden}
body{position:relative;font-family:'Lato',sans-serif;color:var(--ink);background:#dfe9e5}
.abs{position:absolute}
.header{left:0;top:0;width:1200px;height:99px;background:linear-gradient(#fff,#f0f1f1)}
.header-rule{left:0;top:99px;width:1200px;height:6px;background:var(--green)}
.brand{left:192px;top:22px;font:900 50px/1 'Lato',sans-serif;color:var(--green);letter-spacing:1px}
.header-phone{left:838px;top:22px;display:flex;align-items:center;gap:12px;font-size:19px;color:#444}
.nav{left:627px;top:76px;display:flex;height:23px}
.nav a{font-weight:700;font-size:14.5px;color:#555;text-decoration:none;padding:3px 15px 0;height:23px;border-right:3px solid var(--green)}
.nav a:last-child{border-right:none}
.nav a.active{background:var(--green);color:#fff;border-right:none}
.hero{left:0;top:105px;width:1200px;height:620px;background:linear-gradient(180deg,#3f79c2 0%,#8fb0d6 30%,#e6dcc8 55%,#d8d2bf 72%,#b7c7a6 85%,#dfe9e5 100%)}
.arrow{width:82px;height:87px;background:linear-gradient(90deg,rgba(255,255,255,.35),rgba(255,255,255,0));border-radius:5px;display:flex;align-items:center;justify-content:center}
.arrow.next{background:linear-gradient(270deg,rgba(255,255,255,.35),rgba(255,255,255,0))}
.promo-top{left:294px;top:205px;width:612px;height:53px;background:rgba(255,255,255,.82);text-align:center;font-size:24px;line-height:53px;color:#333}
.promo-top em{font-style:normal;color:var(--green)}
.promo{left:294px;top:262px;width:612px;height:115px;background:rgba(255,255,255,.82)}
.markets{left:26px;top:20px;display:flex;gap:28px;font-weight:900;font-size:21px;color:#333}
.markets span{display:flex;align-items:center;gap:8px}
.promo-call{left:104px;top:55px;display:flex;align-items:baseline;gap:6px}
.promo-call b{font-size:17px;color:var(--green);font-weight:700}
.promo-call span{font-size:40px;color:#333;letter-spacing:1px}
.panel{left:199px;top:474px;width:801px;height:347px;background:rgba(255,255,255,.93);border:1px solid var(--line)}
.welcome{left:190px;top:486px;width:820px;height:47px;background:linear-gradient(#0a8d52,var(--green-dark));font:400 25px/47px 'Merriweather',serif;color:#fff;padding-left:16px;letter-spacing:.5px}
.fold{top:533px;width:0;height:0;border-top:6px solid var(--green-deep)}
.fold.l{left:190px;border-left:9px solid transparent}
.fold.r{left:1001px;border-right:9px solid transparent}
.intro{left:226px;top:552px;width:750px;font-size:11.5px;line-height:19.2px;color:#444}
.btn{left:227px;top:642px;width:73px;height:22px;background:var(--green);border:2px solid #cfe3d8;outline:1px solid var(--green);border-radius:3px;color:#fff;font-size:11px;line-height:18px;text-align:center}
.help{left:228px;top:684px;font-size:22px;color:var(--green)}
.col{top:726px}
.col h3{display:flex;align-items:center;gap:8px;font-size:15px;font-weight:400;color:#444}
.col h3 b{color:var(--green);font-weight:700}
.col p{margin-top:8px;font-size:11.5px;line-height:16px;color:var(--muted)}
.divider{top:724px;width:2px;height:84px;background:linear-gradient(rgba(200,200,200,0),#c9c9c9,rgba(200,200,200,0))}
.socials{display:flex;gap:5px;margin-top:6px}
.socials i{width:19px;height:19px;border-radius:4px;display:block}
.footer{left:0;top:844px;width:1200px;height:116px;background:var(--green);color:#fff}
.footer-links{left:0;top:856px;width:1200px;text-align:center;font-size:11.5px;color:#fff}
.footer-rule{left:0;top:886px;width:1200px;height:1px;background:#0b9a58}
.contact-row{left:0;top:903px;width:1200px;display:flex;justify-content:center;gap:24px;font-size:12.5px;font-weight:700;color:#fff}
.contact-row span{display:flex;align-items:center;gap:8px}
.copyright{left:0;top:929px;width:1200px;text-align:center;font-size:11px;color:#fff}
</style>
</head>
<body>
<header class="abs header"></header>
<div class="abs brand">CRB</div>
<div class="abs header-phone">
  <svg width="22" height="16" viewBox="0 0 22 16"><path d="M1 6c0-4 20-4 20 0v2h-5V5H6v3H1z" fill="#00854a"/><rect x="4" y="8" width="14" height="8" rx="1" fill="#00854a"/><circle cx="11" cy="12" r="2.3" fill="#fff"/></svg>
  <span>000-000-1234</span>
</div>
<nav class="abs nav">
  <a class="active">Home</a><a>About CRB</a><a>Properties</a><a>Contact Us</a>
</nav>
<div class="abs header-rule"></div>

<div class="abs hero" role="img" aria-label="Photograph of a domed capitol building under a blue sky with trees"></div>
<div class="abs arrow prev" style="left:90px;top:238px"><svg width="34" height="44"><path d="M28 4 8 22l20 18" stroke="#3a6fb5" stroke-width="6" fill="none"/></svg></div>
<div class="abs arrow next" style="left:1026px;top:238px"><svg width="34" height="44"><path d="M6 4l20 18L6 40" stroke="#9bb5d8" stroke-width="6" fill="none"/></svg></div>

<div class="abs promo-top">Are you looking for a <em>Commercial Properties</em> in?</div>
<div class="abs promo">
  <div class="abs markets">
    <span><svg width="19" height="19" viewBox="0 0 20 20"><circle cx="10" cy="10" r="8.5" fill="none" stroke="#00854a" stroke-width="2"/><circle cx="9" cy="9" r="3.5" fill="none" stroke="#00854a" stroke-width="2"/><path d="M11.5 11.5l4 4" stroke="#00854a" stroke-width="2"/></svg>Washington DC</span>
    <span><svg width="19" height="19" viewBox="0 0 20 20"><circle cx="10" cy="10" r="8.5" fill="none" stroke="#00854a" stroke-width="2"/><circle cx="9" cy="9" r="3.5" fill="none" stroke="#00854a" stroke-width="2"/><path d="M11.5 11.5l4 4" stroke="#00854a" stroke-width="2"/></svg>Maryland</span>
    <span><svg width="19" height="19" viewBox="0 0 20 20"><circle cx="10" cy="10" r="8.5" fill="none" stroke="#00854a" stroke-width="2"/><circle cx="9" cy="9" r="3.5" fill="none" stroke="#00854a" stroke-width="2"/><path d="M11.5 11.5l4 4" stroke="#00854a" stroke-width="2"/></svg>Virginia Market</span>
  </div>
  <div class="abs promo-call"><b>Contact Us On :</b><span>000-000-1234</span></div>
</div>

<section class="abs panel"></section>
<h1 class="abs welcome">Welcome to CRB</h1>
<div class="abs fold l"></div><div class="abs fold r"></div>
<p class="abs intro">Lorem ipsum dolor sit amet, consectetur adipisicing elit, sed do eiusmod tempor incididunt ut labore et dolore magna aliqua. Ut enim ad minim veniam, quis nostrud exercitation ullamco laboris nisi ut aliquip ex ea commodo consequat. Duis aute irure dolor in reprehenderit in voluptate velit esse cillum dolore eu fugiat nulla pariatur. Excepteur sint occaecat cupidatat non proident, sunt in culpa qui officia deserunt mollit anim id est laborum.</p>
<div class="abs btn">Read More ›</div>
<h2 class="abs help">Questions? We're here to help</h2>

<div class="abs col" style="left:228px">
  <h3><svg width="24" height="14" viewBox="0 0 24 14"><rect width="24" height="14" fill="#00854a"/><path d="M1 1l11 7 11-7M1 13l8-6M23 13l-8-6" stroke="#fff" fill="none" stroke-width="1.2"/></svg><span><b>Send</b> Email</span></h3>
  <p>Get prompt, friendly replies to your<br>enquiries and requests</p>
</div>
<div class="abs divider" style="left:435px"></div>
<div class="abs col" style="left:462px">
  <h3><svg width="15" height="15" viewBox="0 0 16 16"><path d="M3 1l3 3-2 2c1 2 3 4 6 6l2-2 3 3-2 2C7 15 1 9 1 3z" fill="#00854a"/></svg><span><b>Call</b> Us</span></h3>
  <p>Toll free numbers available<br>9 AM – 5 PM GMT, Mon - Fri</p>
</div>
<div class="abs divider" style="left:634px"></div>
<div class="abs col" style="left:660px">
  <h3><svg width="14" height="14" viewBox="0 0 20 20"><circle cx="10" cy="10" r="8.5" fill="none" stroke="#00854a" stroke-width="2.5"/><circle cx="9" cy="9" r="3.5" fill="none" stroke="#00854a" stroke-width="2.5"/></svg><span><b>Follow</b> Us</span></h3>
  <p>We’re also available on</p>
  <div class="socials"><i style="background:#3b5998"></i><i style="background:#1a74b5"></i><i style="background:#2aa3e0"></i></div>
</div>

<footer class="abs footer"></footer>
<div class="abs footer-links">Home | About CRB | Properties | Contact Us</div>
<div class="abs footer-rule"></div>
<div class="abs contact-row">
  <span><svg width="9" height="13" viewBox="0 0 10 14"><path d="M5 0a5 5 0 0 1 5 5c0 4-5 9-5 9S0 9 0 5a5 5 0 0 1 5-5z" fill="#fff"/><circle cx="5" cy="5" r="2" fill="#00854a"/></svg>1450 Linden Street NW, Washington, DC 20001</span>
  <span><svg width="20" height="14" viewBox="0 0 22 16"><path d="M1 6c0-4 20-4 20 0v2h-5V5H6v3H1z" fill="#fff"/><rect x="4" y="8" width="14" height="8" rx="1" fill="#fff"/><circle cx="11" cy="12" r="2.3" fill="#00854a"/></svg>000-000-123</span>
  <span><svg width="22" height="13" viewBox="0 0 24 14"><rect x=".5" y=".5" width="23" height="13" fill="none" stroke="#fff"/><path d="M1 1l11 7 11-7M1 13l8-6M23 13l-8-6" stroke="#fff" fill="none"/></svg>info@crbdc.com</span>
</div>
<div class="abs copyright">Copyright © 2013 www.crbdc.com, All Rights Reserved.</div>
</body>
</html>
```